Template for management consulting firm to use with investors

We need a word template design for delivering content to our clients. Our firm evaluates people and talent within a business and then provides information back to our clients. Many of the deliverables are word based. But there are charts, org charts, occasionally graphs (for example feedback scores or ratings), and tables that collate comparative information. The data needs to be clear and clean. Colors need to work for both evaluative information (red/yellow/green) and non-evaluative (dark blue to light blue). We'd like to make sure that we include our logo and be able to create a clean table of contents. Most of the design/text should be black/blue with colors for different sections/content.

Target Market(s)

Private equity investors and CEOs

Font styles to use
Serif

Colors
0667aa
3389bc
86beda
d1f1f4

Requirements
Must have
• Ability to do either horizontal or vertical format
• Cover page that is easy to print and has space for both client name and corvantine name
• Styles/headings for different levels
• Bullets and quote styles
• Table of contents
• Chart colors
• Header and footer, ideally with way to carry through client name on each page

```html
<!DOCTYPE html>
<html lang="en">
<head>
<meta charset="utf-8">
<title>Report Page 3</title>
<link rel="stylesheet" href="https://fonts.googleapis.com/css2?family=Arimo:wght@700&family=Tinos:wght@400;700&display=swap">
<style>
  :root {
    --band-blue: #0581bb;
    --bar-blue: #0581bb;
    --bar-green: #00b550;
    --footer-green: #045a2e;
    --brand-navy: #1d4f7c;
    --ink: #111111;
    --muted: #595959;
    --grid: #d9d9d9;
    --frame: #d0d0d0;
    --paper: #ffffff;
  }
  html, body {
    margin: 0;
    padding: 0;
    width: 930px;
    height: 1200px;
    overflow: hidden;
    background: var(--paper);
  }
  .page {
    position: relative;
    width: 930px;
    height: 1200px;
  }
  .page-border {
    position: absolute;
    left: 43px;
    top: 43px;
    width: 837px;
    height: 1106px;
    border: 1.6px solid var(--ink);
  }
  .client-name {
    position: absolute;
    right: 70px;
    top: 60px;
    font: 400 16.5px/1 "Tinos", serif;
    color: var(--ink);
  }
  .section-band {
    position: absolute;
    left: 100px;
    width: 726px;
    height: 32px;
    background: var(--band-blue);
    color: #fff;
    font: 700 15.5px/32px "Arimo", sans-serif;
    padding-left: 9px;
    box-sizing: border-box;
    letter-spacing: 0.2px;
  }
  .band-lists { top: 108px; }
  .band-charts { top: 596px; }
  .pyramid-diagram, .bar-chart {
    position: absolute;
    left: 0;
    top: 0;
  }
  .chart-text { font-family: "Tinos", serif; fill: var(--muted); }
  .page-number {
    position: absolute;
    left: 56px;
    top: 1099px;
    width: 214px;
    height: 41px;
    background: var(--footer-green);
    color: #fff;
    font: 700 20px/41px "Tinos", serif;
    text-align: center;
  }
  .brand {
    position: absolute;
    left: 762px;
    top: 1102px;
    display: flex;
    align-items: center;
    gap: 6px;
    font: 400 14px/1 "Tinos", serif;
    color: var(--brand-navy);
    letter-spacing: 0.5px;
  }
  .brand-mark {
    width: 8px;
    height: 8px;
    background: var(--brand-navy);
  }
</style>
</head>
<body>
<div class="page">
  <div class="page-border"></div>
  <div class="client-name">Clients Name</div>

  <div class="section-band band-lists">ADD LISTS DATA</div>

  <svg class="pyramid-diagram" width="930" height="560" viewBox="0 0 930 560">
    <defs>
      <linearGradient id="pyramidFill" x1="0" y1="0" x2="0" y2="1">
        <stop offset="0" stop-color="#4b95c9"/>
        <stop offset="0.5" stop-color="#0585c0"/>
        <stop offset="1" stop-color="#0775b1"/>
      </linearGradient>
      <filter id="softShadow" x="-10%" y="-10%" width="120%" height="120%">
        <feDropShadow dx="0" dy="2" stdDeviation="2" flood-opacity="0.3"/>
      </filter>
    </defs>
    <polygon points="357,154 199,470 516,470" fill="url(#pyramidFill)" filter="url(#softShadow)"/>
    <g fill="#ffffff" fill-opacity="0.9" stroke="#0581bb" stroke-width="1">
      <rect class="list-box" x="358" y="186" width="206" height="74" rx="11"/>
      <rect class="list-box" x="358" y="270" width="206" height="75" rx="11"/>
      <rect class="list-box" x="358" y="354" width="206" height="75" rx="11"/>
    </g>
  </svg>

  <div class="section-band band-charts">CHARTS</div>

  <svg class="bar-chart" width="930" height="1000" viewBox="0 0 930 1000">
    <rect x="178" y="666" width="545" height="317" fill="#fff" stroke="var(--frame)" stroke-width="1.2"/>
    <text class="chart-text" x="450" y="698" font-size="20" text-anchor="middle">Chart Title</text>

    <g stroke="var(--grid)" stroke-width="1">
      <line x1="206" y1="721" x2="706" y2="721"/>
      <line x1="206" y1="754" x2="706" y2="754"/>
      <line x1="206" y1="787" x2="706" y2="787"/>
      <line x1="206" y1="819" x2="706" y2="819"/>
      <line x1="206" y1="852" x2="706" y2="852"/>
      <line x1="206" y1="885" x2="706" y2="885"/>
      <line x1="206" y1="917" x2="706" y2="917"/>
    </g>
    <g class="chart-text" font-size="12" text-anchor="middle">
      <text x="191" y="725">6</text>
      <text x="191" y="758">5</text>
      <text x="191" y="791">4</text>
      <text x="191" y="823">3</text>
      <text x="191" y="856">2</text>
      <text x="191" y="889">1</text>
      <text x="191" y="921">0</text>
    </g>

    <g class="series-1" fill="var(--bar-blue)">
      <rect x="230" y="776.4" width="22" height="140.6"/>
      <rect x="355" y="835.2" width="22" height="81.8"/>
      <rect x="479.5" y="802.6" width="22" height="114.4"/>
      <rect x="604" y="769.9" width="22" height="147.1"/>
    </g>
    <g class="series-2" fill="var(--bar-green)">
      <rect x="258" y="838.5" width="22" height="78.5"/>
      <rect x="383" y="773.1" width="22" height="143.9"/>
      <rect x="507.5" y="858.1" width="22" height="58.9"/>
      <rect x="632" y="825.4" width="22" height="91.6"/>
    </g>
    <g class="series-3" fill="var(--bar-blue)">
      <rect x="285.5" y="851.6" width="22" height="65.4"/>
      <rect x="410.5" y="851.6" width="22" height="65.4"/>
      <rect x="535" y="818.9" width="22" height="98.1"/>
      <rect x="659.5" y="753.5" width="22" height="163.5"/>
    </g>

    <g class="chart-text" font-size="13" text-anchor="middle">
      <text x="268.5" y="938">Category 1</text>
      <text x="394" y="938">Category 2</text>
      <text x="518.6" y="938">Category 3</text>
      <text x="643.8" y="938">Category 4</text>
    </g>

    <g class="chart-text" font-size="13">
      <rect x="361" y="958" width="7" height="7" fill="var(--bar-blue)"/>
      <text x="371" y="967">Series 1</text>
      <rect x="426.5" y="958" width="7" height="7" fill="var(--bar-green)"/>
      <text x="436.5" y="967">Series 2</text>
      <rect x="492" y="958" width="7" height="7" fill="var(--bar-blue)"/>
      <text x="502" y="967">Series 3</text>
    </g>
  </svg>

  <div class="page-number">3</div>
  <div class="brand"><span class="brand-mark"></span>CORVANTINE</div>
</div>
</body>
</html>
```